Business Card Design with new logo

Dorian Pelleway 4172
E 118th St Brenford, IL 62011
Cell: 217-555-0193
pellewayrestoration@mailvane.test

Classic Car Restoration Services Buy Sell Trade Consign

Dorian Pelleway 9698
Cell: 217-555-0193

```html
<!DOCTYPE html>
<html lang="en">
<head>
<meta charset="utf-8">
<title>Pelleway Restoration LLC – Business Card</title>
<link rel="stylesheet" href="https://fonts.googleapis.com/css2?family=Didact+Gothic&display=swap">
<style>
  :root {
    --backdrop: #e9ebed;
    --card: #ffffff;
    --card-inner: #f7f7f6;
    --brand-red: #e03a3c;
    --ink: #2b2f33;
    --ink-soft: #4a4f55;
  }
  * { box-sizing: border-box; margin: 0; padding: 0; }
  html, body {
    width: 1200px;
    height: 800px;
    overflow: hidden;
  }
  body {
    background: var(--backdrop);
    font-family: "Didact Gothic", "Century Gothic", sans-serif;
    color: var(--ink);
  }
  .card-set {
    position: absolute;
    top: 252px;
    left: 60px;
    display: flex;
    gap: 40px;
  }
  .card {
    width: 520px;
    height: 297px;
    background: var(--card);
    box-shadow: 0 2px 10px rgba(0,0,0,0.08);
  }

  /* Front */
  .card-front {
    display: flex;
    align-items: center;
    justify-content: center;
  }
  .brand {
    display: flex;
    align-items: center;
    gap: 14px;
    color: var(--brand-red);
    font-weight: 400;
  }
  .brand-dot {
    width: 34px;
    height: 34px;
    border-radius: 50%;
    background: var(--brand-red);
  }
  .brand-name {
    font-size: 27px;
    letter-spacing: 0.06em;
    text-transform: uppercase;
    line-height: 1.15;
  }

  /* Back */
  .card-back {
    background: var(--brand-red);
    padding: 24px;
  }
  .card-back-inner {
    width: 100%;
    height: 100%;
    background: var(--card-inner);
    display: flex;
    flex-direction: column;
    align-items: center;
    justify-content: center;
    text-align: center;
    font-size: 12px;
    color: var(--ink-soft);
  }
  .contact-name {
    font-size: 13px;
    font-weight: 700;
    color: var(--ink);
    margin-bottom: 14px;
  }
  .contact-phone { margin-bottom: 26px; }
  .contact-email { margin-bottom: 12px; }
  .contact-address { line-height: 1.6; }
</style>
</head>
<body>
  <main class="card-set">
    <section class="card card-front">
      <div class="brand">
        <span class="brand-dot"></span>
        <span class="brand-name">Pelleway<br>Restoration LLC</span>
      </div>
    </section>

    <section class="card card-back">
      <div class="card-back-inner">
        <p class="contact-name">Dorian Pelleway</p>
        <p class="contact-phone">Cell: 217-555-0193</p>
        <p class="contact-email">pellewayrestoration@mailvane.test</p>
        <p class="contact-address">E 118th St Brenford,<br>IL 62011</p>
      </div>
    </section>
  </main>
</body>
</html>
```